Boutique Recruiting Firm Needs Eye-Catching Business Cards (and potentially new logo)!

I run a recruiting company in Charleston, South Carolina. I have a ton of networking events coming up and need business cards to grab potential clients attention.

I currently have a logo but if you want to try and recreate the logo to something more modern I am open to that. If you do decide to create a new logo please submit the business card with the old logo and the new one.

Staffing Under Blue Lanterns, LLC is the name of my company. I create videos to my clients and candidates which allows me to standout from my competition so I would like a business card (and possibly new logo) to do the same.

I do not specialize in any one industry of recruiting.

```html
<!DOCTYPE html>
<html lang="en">
<head>
<meta charset="utf-8">
<title>Staffing Under Blue Lanterns – Business Card</title>
<link rel="stylesheet" href="https://fonts.googleapis.com/css2?family=Old+Standard+TT:wght@700&family=Arimo:wght@400&display=swap">
<style>
  :root {
    --page-bg: #e8e5e1;
    --card-light: #f1f0ee;
    --card-light-edge: #d9d6d3;
    --band-dark: #161616;
    --ink: #2a2a2a;
    --ink-soft: #3c3c3c;
    --contact-gold: #c7b195;
    --icon-bg: #cfcac4;
    --icon-ink: #1a1a1a;
  }
  * { margin: 0; padding: 0; box-sizing: border-box; }
  html, body {
    width: 1200px;
    height: 970px;
    overflow: hidden;
    background: var(--page-bg);
  }
  .business-card {
    position: absolute;
    left: 100px;
    top: 187px;
    width: 1000px;
    height: 596px;
    background: linear-gradient(160deg, var(--card-light) 0%, #e6e4e1 60%, var(--card-light-edge) 100%);
    box-shadow: 0 10px 30px rgba(0,0,0,0.18);
    overflow: hidden;
  }
  .card-band {
    position: absolute;
    inset: 0;
    width: 100%;
    height: 100%;
  }
  .company-name {
    position: absolute;
    left: 53px;
    top: 56px;
    font-family: "Old Standard TT", serif;
    font-weight: 700;
    font-size: 50px;
    line-height: 1.08;
    color: var(--ink);
  }
  .person {
    position: absolute;
    left: 53px;
    top: 286px;
  }
  .person-name {
    font-family: "Old Standard TT", serif;
    font-weight: 700;
    font-size: 38px;
    color: var(--ink-soft);
    line-height: 1.1;
  }
  .person-title {
    font-family: "Arimo", sans-serif;
    font-size: 24px;
    color: var(--ink);
    margin-top: 4px;
  }
  .contact-list {
    position: absolute;
    right: 46px;
    top: 388px;
    list-style: none;
  }
  .contact-item {
    display: flex;
    align-items: center;
    justify-content: flex-end;
    height: 44px;
    font-family: "Arimo", sans-serif;
    font-size: 24px;
    color: var(--contact-gold);
  }
  .contact-icon {
    width: 20px;
    height: 20px;
    margin-left: 20px;
    flex: none;
  }
</style>
</head>
<body>
  <div class="business-card">
    <svg class="card-band" viewBox="0 0 1000 596" preserveAspectRatio="none" aria-hidden="true">
      <path d="M0,560 C400,540 620,220 1000,170 L1000,596 L0,596 Z" fill="var(--band-dark)"/>
    </svg>

    <div class="company-name">Staffing Under<br>Blue Lanterns, LLC</div>

    <div class="person">
      <div class="person-name">Marissa Delane</div>
      <div class="person-title">Founder / Executive Recruiter</div>
    </div>

    <ul class="contact-list">
      <li class="contact-item">843 555 0142
        <svg class="contact-icon" viewBox="0 0 20 20" aria-hidden="true">
          <rect width="20" height="20" rx="2" fill="var(--icon-bg)"/>
          <path d="M5 7 Q10 3 15 7 L14 9 L12 8 L12 7 Q10 6 8 7 L8 8 L6 9 Z M6 11 H14 V15 H6 Z" fill="var(--icon-ink)"/>
        </svg>
      </li>
      <li class="contact-item">www.bluelanterns.com
        <svg class="contact-icon" viewBox="0 0 20 20" aria-hidden="true">
          <rect width="20" height="20" rx="2" fill="var(--icon-bg)"/>
          <circle cx="10" cy="10" r="6" fill="none" stroke="var(--icon-ink)" stroke-width="1.6"/>
          <path d="M4 10 H16 M10 4 Q6 10 10 16 M10 4 Q14 10 10 16" fill="none" stroke="var(--icon-ink)" stroke-width="1.2"/>
        </svg>
      </li>
      <li class="contact-item">hello@bluelanterns.com
        <svg class="contact-icon" viewBox="0 0 20 20" aria-hidden="true">
          <rect width="20" height="20" rx="2" fill="var(--icon-bg)"/>
          <rect x="4" y="6" width="12" height="8" fill="var(--icon-ink)"/>
          <path d="M4 6 L10 11 L16 6" fill="none" stroke="var(--icon-bg)" stroke-width="1.2"/>
        </svg>
      </li>
      <li class="contact-item">214 Harbor Lane, Charleston, SC 29401
        <svg class="contact-icon" viewBox="0 0 20 20" aria-hidden="true">
          <rect width="20" height="20" rx="2" fill="var(--icon-bg)"/>
          <path d="M10 16 C6 11 6 9 6 8 A4 4 0 0 1 14 8 C14 9 14 11 10 16 Z" fill="var(--icon-ink)"/>
          <circle cx="10" cy="8" r="1.6" fill="var(--icon-bg)"/>
        </svg>
      </li>
    </ul>
  </div>
</body>
</html>
```